Lawnmowing and maintenance business card and letterhead design

We need a business card design and a letter head design for a new company we are starting up.

I would like to include pictures of a cartoon ride on mower with a few tools on board, a cartoon person vacuuming staircase and a cartoon person dusting.

Our business will be handling looking after unit public areas, ie garden maintenance - mowing, trimming trees, blowing leaves.
Also dusting, vacuuming, window cleaning.

Industry/Entity Type

Business

Contact Information for Business Card

Tolvane lawnmowing and property maintenance
14 Barlowe Crescent
Mount Pritchard NSW 2170
0491726048
0478301652

Requirements
Must have
• Must have the business name, business address, abn number 64 907 518 243, business phone numbers pictures as above

```html
<!DOCTYPE html>
<html lang="en">
<head>
<meta charset="utf-8">
<title>Tolvane – Letterhead and Business Card</title>
<link rel="stylesheet" href="https://fonts.googleapis.com/css2?family=Didact+Gothic&family=Tinos:wght@400;700&display=swap">
<style>
  :root {
    --backdrop: #2a2a2a;
    --paper: #ffffff;
    --paper-shade: #e6e6e6;
    --brand-green: #74b62e;
    --ink: #1c1c1c;
    --ink-soft: #4a4a4a;
  }
  * { box-sizing: border-box; margin: 0; padding: 0; }
  html, body {
    width: 1200px;
    height: 900px;
    overflow: hidden;
    background: var(--backdrop);
  }
  .stationery {
    position: relative;
    width: 1200px;
    height: 900px;
  }

  /* ---------- Letterhead ---------- */
  .letterhead {
    position: absolute;
    left: 60px;
    top: 40px;
    width: 580px;
    height: 820px;
    background: linear-gradient(160deg, var(--paper) 0%, var(--paper) 45%, var(--paper-shade) 100%);
    box-shadow: 0 10px 30px rgba(0,0,0,.5);
  }
  .letterhead__bar {
    position: absolute;
    left: 0;
    top: 150px;
    bottom: 0;
    width: 12px;
    background: var(--brand-green);
  }
  .brand-name {
    font-family: "Didact Gothic", sans-serif;
    font-weight: 400;
    color: var(--brand-green);
    letter-spacing: 2px;
    line-height: 1;
  }
  .brand-tagline {
    font-family: "Didact Gothic", sans-serif;
    color: var(--ink-soft);
    letter-spacing: .5px;
    white-space: nowrap;
  }
  .letterhead .brand-name {
    position: absolute;
    left: 22px;
    top: 105px;
    font-size: 92px;
  }
  .letterhead .brand-tagline {
    position: absolute;
    left: 96px;
    top: 205px;
    font-size: 19px;
  }
  .letterhead__footer {
    position: absolute;
    right: 36px;
    bottom: 44px;
    font-family: "Tinos", serif;
    color: var(--ink);
  }
  .letterhead__contact-line {
    font-size: 14px;
    display: flex;
    align-items: center;
    gap: 8px;
    white-space: nowrap;
  }
  .dot {
    display: inline-block;
    width: 9px;
    height: 9px;
    border-radius: 50%;
    background: var(--brand-green);
  }
  .letterhead__abn {
    margin-top: 6px;
    margin-left: 78px;
    font-size: 17px;
  }
  .label {
    font-family: "Tinos", serif;
    font-weight: 700;
    color: var(--brand-green);
    text-transform: uppercase;
  }

  /* ---------- Business card ---------- */
  .business-card {
    position: absolute;
    left: 670px;
    top: 260px;
    width: 500px;
    height: 300px;
    background: linear-gradient(170deg, var(--paper) 0%, var(--paper) 55%, var(--paper-shade) 100%);
    box-shadow: 0 10px 26px rgba(0,0,0,.55);
    overflow: hidden;
  }
  .business-card__bar {
    position: absolute;
    left: 0;
    top: 0;
    bottom: 0;
    width: 9px;
    background: var(--brand-green);
  }
  .business-card .brand-name {
    position: absolute;
    left: 16px;
    top: 40px;
    font-size: 50px;
  }
  .business-card .brand-tagline {
    position: absolute;
    left: 58px;
    top: 96px;
    font-size: 11px;
  }
  .business-card__details {
    position: absolute;
    left: 150px;
    top: 124px;
    width: 200px;
    font-family: "Tinos", serif;
    color: var(--ink);
    font-size: 12.5px;
    line-height: 1.25;
  }
  .business-card__details .label {
    font-size: 12.5px;
    margin-top: 9px;
  }
  .business-card__details .label:first-child { margin-top: 0; }
  .business-card__details .value { font-weight: 700; white-space: nowrap; }
  .business-card__details .value--indent,
  .business-card__details .label--indent { margin-left: 84px; }
  .business-card__art {
    position: absolute;
    right: 12px;
    top: 12px;
    width: 130px;
    height: 276px;
  }
</style>
</head>
<body>
<main class="stationery">

  <section class="letterhead" aria-label="Letterhead">
    <div class="letterhead__bar"></div>
    <h1 class="brand-name">TOLVANE</h1>
    <p class="brand-tagline">lawnmowing and property maintenance</p>
    <footer class="letterhead__footer">
      <p class="letterhead__contact-line">
        <span>14 Barlowe Crescent Mount Pritchard NSW 2170</span>
        <span class="dot"></span>
        <span>0491726048</span>
        <span class="dot"></span>
        <span>0478301652</span>
      </p>
      <p class="letterhead__abn"><span class="label">ABN Number</span>&nbsp; 64 907 518 243</p>
    </footer>
  </section>

  <section class="business-card" aria-label="Business card">
    <div class="business-card__bar"></div>
    <h2 class="brand-name">TOLVANE</h2>
    <p class="brand-tagline">lawnmowing and property maintenance</p>
    <div class="business-card__details">
      <p class="label">Business Address</p>
      <p class="value">14 Barlowe Crescent</p>
      <p class="value">Mount Pritchard NSW 2170</p>
      <p class="label label--indent">Phone No.</p>
      <p class="value value--indent">0491726048</p>
      <p class="value value--indent">0478301652</p>
      <p class="label label--indent">ABN Number</p>
      <p class="value value--indent">64 907 518 243</p>
    </div>
    <svg class="business-card__art" viewBox="0 0 130 276" role="img"
         aria-label="Cartoon illustrations: a person dusting at a table, a person mowing the lawn on green grass, and a person vacuuming">
      <defs>
        <linearGradient id="art-fill" x1="0" y1="0" x2="0" y2="1">
          <stop offset="0" stop-color="#eef1ea"/>
          <stop offset="0.45" stop-color="#dfe9d2"/>
          <stop offset="0.55" stop-color="#a6cf6f"/>
          <stop offset="0.62" stop-color="#dfe9d2"/>
          <stop offset="1" stop-color="#e4e6e2"/>
        </linearGradient>
      </defs>
      <rect width="130" height="276" rx="6" fill="url(#art-fill)"/>
    </svg>
  </section>

</main>
</body>
</html>
```